Criação de Kit com 6 Layouts de Post para Redes Sociais (Facebook, Instagram e etc) + Capa de Facebook para Saúde & Nutrição
" Atendimentos e procedimentos em consultório Atendimento de consultas cirurgicas: cir geral / cir aparelho digestivo / urologia / cir de cabeça e pescoço Atendimento de consultas clínicas: clínica médica / cardiologia / endocrinologia Outros atendimentos: Fisioterapia / nutrição / estética "

```html
<!DOCTYPE html>
<html lang="pt-BR">
<head>
<meta charset="UTF-8">
<title>Clínica Vellora — Priorize seu bem-estar</title>
<link rel="stylesheet" href="https://fonts.googleapis.com/css2?family=Montserrat:wght@500;700;800&display=swap">
<style>
  :root {
    --navy-deep: #0a1633;
    --navy: #13264f;
    --scrub-blue: #3a6fb3;
    --scrub-light: #7fb0e6;
    --gold: #d8b667;
    --white: #ffffff;
  }
  * { margin: 0; padding: 0; box-sizing: border-box; }
  html, body { width: 1200px; height: 1200px; overflow: hidden; background: var(--navy-deep); }
  .post {
    position: relative;
    width: 1200px;
    height: 1200px;
    overflow: hidden;
    font-family: "Montserrat", sans-serif;
    color: var(--white);
  }
  .surgery-photo {
    position: absolute;
    inset: 0;
    background:
      radial-gradient(ellipse 420px 360px at 330px 900px, rgba(190,225,255,0.55), transparent 70%),
      radial-gradient(ellipse 520px 620px at 300px 620px, var(--scrub-blue), transparent 75%),
      radial-gradient(ellipse 300px 260px at 120px 150px, rgba(90,150,210,0.7), transparent 75%),
      linear-gradient(100deg, #2c5a98 0%, #1b3a72 35%, var(--navy) 55%, var(--navy-deep) 100%);
  }
  .brand {
    position: absolute;
    left: 532px;
    top: 130px;
    width: 400px;
    text-align: center;
    color: var(--gold);
    font-weight: 500;
  }
  .brand-dot {
    display: block;
    width: 70px;
    height: 70px;
    margin: 0 auto 28px;
    border-radius: 50%;
    background: var(--gold);
  }
  .brand-name { font-size: 50px; line-height: 1.1; letter-spacing: 2px; }
  .headline {
    position: absolute;
    left: 556px;
    top: 462px;
    font-size: 86px;
    font-weight: 800;
    line-height: 1.12;
    letter-spacing: -1px;
  }
  .lead {
    position: absolute;
    left: 558px;
    top: 672px;
    font-size: 35px;
    font-weight: 500;
    line-height: 65px;
  }
  .contact-pill {
    position: absolute;
    left: 562px;
    top: 907px;
    width: 392px;
    height: 60px;
    border: 3px solid var(--white);
    border-radius: 30px;
    display: flex;
    align-items: center;
    justify-content: center;
    gap: 14px;
    font-size: 27px;
    font-weight: 700;
  }
  .contact-pill svg { width: 30px; height: 30px; }
  .social-actions {
    position: absolute;
    left: 98px;
    top: 1052px;
    display: flex;
    gap: 48px;
  }
  .social-actions svg { width: 54px; height: 54px; }
  .save-icon { position: absolute; left: 1060px; top: 1056px; width: 44px; height: 48px; }
</style>
</head>
<body>
  <main class="post">
    <div class="surgery-photo" role="img" aria-label="Equipe cirúrgica em aventais e toucas azuis operando um paciente sob luz fria em sala de cirurgia"></div>

    <div class="brand">
      <span class="brand-dot"></span>
      <div class="brand-name">Clínica<br>VELLORA</div>
    </div>

    <h1 class="headline">Priorize seu<br>bem-estar!</h1>

    <p class="lead">Sua saúde merece o melhor!<br>Descubra a diferença de um<br>atendimento de qualidade.</p>

    <div class="contact-pill">
      <svg viewBox="0 0 24 24" fill="none" stroke="#fff" stroke-width="2" stroke-linecap="round" stroke-linejoin="round"><path d="M22 16.9v3a2 2 0 0 1-2.2 2 19.8 19.8 0 0 1-8.6-3.1 19.5 19.5 0 0 1-6-6A19.8 19.8 0 0 1 2.1 4.2 2 2 0 0 1 4.1 2h3a2 2 0 0 1 2 1.7c.1.9.4 1.8.7 2.7a2 2 0 0 1-.5 2.1L8 9.8a16 16 0 0 0 6 6l1.3-1.3a2 2 0 0 1 2.1-.5c.9.3 1.8.6 2.7.7a2 2 0 0 1 1.7 2z"/></svg>
      <span>(11) 9 4821-3076</span>
    </div>

    <div class="social-actions">
      <svg viewBox="0 0 24 24" fill="none" stroke="var(--gold)" stroke-width="1.6" stroke-linejoin="round"><path d="M12 20.5s-8-4.9-8-10.6A4.4 4.4 0 0 1 12 7a4.4 4.4 0 0 1 8 2.9c0 5.7-8 10.6-8 10.6z"/></svg>
      <svg viewBox="0 0 24 24" fill="none" stroke="var(--gold)" stroke-width="1.6" stroke-linejoin="round"><path d="M20.5 11.5a8.5 8.5 0 1 1-4.2-7.3A8.5 8.5 0 0 1 20.5 11.5zM19 17l1.8 4-4.2-1.6"/></svg>
      <svg viewBox="0 0 24 24" fill="none" stroke="var(--gold)" stroke-width="1.6" stroke-linejoin="round"><path d="M21.5 3 2.5 10.5l7.5 3.2 3.3 7.8L21.5 3zM10 13.7 21.5 3"/></svg>
    </div>

    <svg class="save-icon" viewBox="0 0 22 24"><path d="M2 1h18v22l-9-6-9 6z" fill="var(--gold)"/></svg>
  </main>
</body>
</html>
```